tallkettle.example - youth/backpackers Adventure Travel contact site

Landing Page: Logo, @RidgelineRoamerCrew, Australia | New Zealand | Fiji | South East Asia, Start Button, a Rotating carousel of supplier logos, ©Tall Kettle Travel, Terms and Conditions link, Contact Us page link, social media/contact icons.
Start Button: Takes you to destinations selection Map - Hover over effect with selectable Countries, states, regions, and next & back buttons.
Next Button: Takes you to Activities - Selectable Buttons for Sky Diving, Sailing, Whitewater Rafting, Bungee jumping, camping, hiking, Surfing, Jet Boating, kayaking, canyoning, National Parks, Scuba Diving, Snorkeling and beaches etc., Tandem Hand gliding, with a typable "Have we missed anything you want to experience" area and back and next buttons.
Next Button: Takes you to extras - Selectable buttons for Bus Passes, Accommodation, Car Hire, Camper Hire and back and next buttons.
Next Button: Takes you to enter customer details: Name, Age, Phone, Email, How did you hear about us, Dietary requirement, start & end date, start & end location, Number of Travellers, Budget, anything else area, Submit for your custom adventure button. - All this information then gets emailed.

Target Market(s)

Backpacker/youth adventure travel

Industry/Entity Type

Travel Agent

Coding

Coded - Design and coding required

Number of Pages Required

3 page

Colors

Designer to choose colors to be used in the design.

Requirements
Must have
• Somewhere to be automatically synced Snap profile pictures and videos.
• Full screen, scalable to any device size - 65% of our users use mobile devices.
• Wordpress
Nice to have
• Easy to add and remove selectable buttons
• If you can think of any special feature to add ;)
Should not have
• Basic contact form look

```html
<!DOCTYPE html>
<html lang="en">
<head>
<meta charset="utf-8">
<title>Tall Kettle Travel — Adventure Travel Specialists</title>
<link href="https://fonts.googleapis.com/css2?family=Catamaran:wght@400;500;600;700&display=swap" rel="stylesheet">
<style>
  :root {
    --coral: #f94f45;
    --coral-deep: #c53a31;
    --white: #ffffff;
    --band: #eeeff0;
    --band-text: #6f6f72;
    --dot: #b9b9bc;
    --footer-text: #2a2a2c;
    --sky-glow: #fbe3a6;
    --sun: #f6b24a;
    --ridge: #a8612c;
    --earth: #5b3a22;
    --moss: #6d6a3a;
  }
  * { box-sizing: border-box; margin: 0; padding: 0; }
  html, body { width: 1200px; height: 755px; overflow: hidden; background: var(--white); }
  body { font-family: "Catamaran", sans-serif; position: relative; }

  .hero {
    position: absolute; left: 0; top: 0; width: 1200px; height: 566px; overflow: hidden;
  }
  .hero-photo {
    position: absolute; inset: 0;
    background:
      radial-gradient(ellipse 420px 300px at 800px 60px, var(--sky-glow) 0%, rgba(251,227,166,0) 70%),
      radial-gradient(ellipse 500px 260px at 560px 560px, var(--moss) 0%, rgba(109,106,58,0) 75%),
      linear-gradient(180deg, #f2c98a 0%, var(--sun) 18%, var(--ridge) 45%, var(--earth) 78%, #3b2a1c 100%);
  }
  .hero-shade { position: absolute; inset: 0; background: rgba(40, 20, 10, 0.12); }

  .brand {
    position: absolute; left: 637px; top: 104px; transform: translate(-50%, -50%);
    display: flex; align-items: center; gap: 10px;
  }
  .brand-mark { width: 18px; height: 18px; border-radius: 50%; background: var(--coral); }
  .brand-name {
    font-weight: 700; font-size: 30px; color: var(--coral); white-space: nowrap; line-height: 1;
  }

  .headline {
    position: absolute; left: 0; width: 1200px; top: 268px; text-align: center;
    font-weight: 500; font-size: 52px; color: var(--white); letter-spacing: 1px; line-height: 1.2;
  }
  .regions {
    position: absolute; left: 0; width: 1200px; top: 342px; text-align: center;
    font-weight: 500; font-size: 20px; color: var(--white); letter-spacing: 0.3px;
  }
  .start-button {
    position: absolute; left: 459px; top: 412px; width: 257px; height: 62px;
    border-radius: 31px; background: var(--coral); border: none;
    box-shadow: 0 4px 0 var(--coral-deep);
    color: var(--white); font-family: "Catamaran", sans-serif; font-weight: 500; font-size: 27px;
    display: flex; align-items: center; justify-content: center; cursor: pointer;
  }
  .start-button:hover { background: #ff5f55; }

  .supplier-band {
    position: absolute; left: 0; top: 566px; width: 1200px; height: 128px; background: var(--band);
  }
  .supplier-list {
    position: absolute; left: 148px; right: 190px; top: 42px; height: 40px;
    display: flex; align-items: center; justify-content: space-between; list-style: none;
  }
  .supplier {
    font-weight: 700; font-size: 19px; color: var(--band-text); white-space: nowrap;
  }
  .supplier-pill { display: flex; align-items: center; gap: 6px; }
  .supplier-pill .mark { width: 10px; height: 10px; border-radius: 50%; background: var(--band-text); }
  .carousel-dots {
    position: absolute; top: 103px; left: 575px; display: flex; gap: 8px; list-style: none;
  }
  .carousel-dots li { width: 7px; height: 7px; border-radius: 50%; background: var(--dot); }
  .carousel-dots li.is-active { background: var(--coral); }

  .site-footer {
    position: absolute; left: 0; top: 694px; width: 1200px; height: 61px;
    font-size: 11px; font-weight: 500; color: var(--footer-text);
  }
  .site-footer > * { position: absolute; top: 24px; line-height: 14px; }
  .copyright { left: 90px; }
  .footer-links { left: 383px; display: flex; align-items: center; gap: 4px; }
  .footer-links a { color: var(--footer-text); text-decoration: none; }
  .footer-links svg { width: 10px; height: 10px; fill: var(--coral); }
  .get-in-touch { left: 926px; display: flex; align-items: center; gap: 12px; }
  .social { display: flex; align-items: center; gap: 10px; }
  .social a { color: var(--footer-text); text-decoration: none; font-weight: 700; font-size: 10px; }
  .social a.first { color: var(--coral); }
  .social svg { width: 12px; height: 10px; fill: none; stroke: var(--footer-text); stroke-width: 1.4; display: block; }
</style>
</head>
<body>
  <header class="hero">
    <div class="hero-photo" role="img" aria-label="Hiker standing on a mossy rock overlooking sunlit mountain ridges at sunset"></div>
    <div class="hero-shade"></div>
    <div class="brand">
      <span class="brand-mark"></span>
      <span class="brand-name">Tall Kettle Travel</span>
    </div>
    <h1 class="headline">Adventure Travel Specialists</h1>
    <p class="regions">Australia | New Zealand | Fiji | South East Asia</p>
    <button class="start-button" type="button">Start</button>
  </header>

  <section class="supplier-band" aria-label="Our suppliers">
    <ul class="supplier-list">
      <li class="supplier">Harbour Heat</li>
      <li class="supplier">leafline</li>
      <li class="supplier">Voltra</li>
      <li class="supplier">Ampere</li>
      <li class="supplier">prime:grid</li>
      <li class="supplier supplier-pill"><span class="mark"></span>Bright Current</li>
      <li class="supplier">Low Ember</li>
      <li class="supplier">kiloway</li>
    </ul>
    <ul class="carousel-dots">
      <li class="is-active"></li><li></li><li></li><li></li>
    </ul>
  </section>

  <footer class="site-footer">
    <p class="copyright">© 2017 Company Name &nbsp;|&nbsp; All Rights Reserved</p>
    <nav class="footer-links">
      <a href="#">Terms and Conditions</a> |
      <svg viewBox="0 0 24 24" aria-hidden="true"><path d="M6.6 10.8a15.1 15.1 0 0 0 6.6 6.6l2.2-2.2a1 1 0 0 1 1-.25 11.4 11.4 0 0 0 3.6.57 1 1 0 0 1 1 1V20a1 1 0 0 1-1 1A17 17 0 0 1 3 4a1 1 0 0 1 1-1h3.5a1 1 0 0 1 1 1c0 1.25.2 2.45.57 3.6a1 1 0 0 1-.25 1z"/></svg>
      <a href="#">Contact Us</a>
    </nav>
    <div class="get-in-touch">
      <span>Get In Touch</span>
      <div class="social">
        <a class="first" href="#">Yarn</a>
        <a href="#" aria-label="Email"><svg viewBox="0 0 14 11"><rect x="0.7" y="0.7" width="12.6" height="9.6" rx="1"/><path d="M1 1.2 7 6l6-4.8"/></svg></a>
        <a href="#">Snap</a>
        <a href="#">Reel</a>
      </div>
    </div>
  </footer>
</body>
</html>
```